Kiosk Coin Venture: Safe and Secure Cash Money

Front of card: LOGO

Back of card:
$$$ FREE ATM PLACEMENT $$$
BENIFITS OF HAVING AN ATM AT YOUR BUSINESS
FREE ATM and BTM (Bitcoin) installation, maintenance, and loading.
Lower card processing fees
Stimulate more traffic.
Ease of access for customers
Maintain customers inside location.
Higher tips and spending

Contact me for more information!
Name: Tobias Merlano
Phone: (512) 638-9071 - Call or Text
Email: Tobias@KioskCoin.example

Contact Information for Business Card

The card should be shape of the logo. Only the back will have all the contact and business details.

Requirements
Must have
• The logo itself will be one side, the card will be the shape of the logo. contact details on back side.

```html
<!DOCTYPE html>
<html lang="en">
<head>
<meta charset="utf-8">
<title>Kiosk Coin Venture – Business Card</title>
<link href="https://fonts.googleapis.com/css2?family=Oswald:wght@500;600&family=Lato:wght@300;400;700&display=swap" rel="stylesheet">
<style>
  :root {
    --page: #e8e8e8;
    --ink: #111111;
    --paper: #ffffff;
    --steel-light: #d9d9d9;
    --steel-dark: #8a8a8a;
    --shield-dark: #161616;
    --gold: #d9b53a;
    --gold-deep: #b8931f;
  }
  html, body { margin: 0; padding: 0; }
  body {
    width: 1200px; height: 900px; overflow: hidden;
    background: var(--page);
    position: relative;
    font-family: "Lato", Arial, sans-serif;
    color: var(--ink);
  }
  .card { position: absolute; }
  .card svg.card-shape { position: absolute; inset: 0; display: block; }

  /* Back side */
  .card-back { left: 132px; top: 136px; width: 422px; height: 628px; }
  .card-back .line {
    position: absolute; left: 0; width: 100%;
    text-align: center; white-space: nowrap;
    transform: translateY(-50%);
  }
  .headline {
    font-family: "Oswald", "Arial Narrow", sans-serif;
    font-weight: 600; font-size: 31px; letter-spacing: -0.5px;
    transform: translateY(-50%) scaleX(0.86) !important;
  }
  .benefits-band {
    position: absolute; left: 8px; right: 8px; top: 149px; height: 40px;
    background: var(--ink); color: var(--paper);
    font-family: "Oswald", "Arial Narrow", sans-serif;
    font-weight: 500; font-size: 24px; letter-spacing: -0.3px;
    display: flex; align-items: center; justify-content: center;
    white-space: nowrap;
  }
  .benefits-band span { display: inline-block; transform: scaleX(0.84); }
  .benefit { font-size: 16px; }
  .benefit.light { font-weight: 300; }
  .benefit.regular { font-weight: 400; }
  .contact-heading { font-weight: 700; font-size: 16px; }
  .owner-name { font-weight: 700; font-size: 31px; }
  .owner-title { font-size: 16px; letter-spacing: 0.3px; }
  .divider {
    position: absolute; left: 90px; right: 98px; top: 495px;
    display: flex; align-items: center; gap: 6px;
    transform: translateY(-50%);
  }
  .divider .rule { flex: 1; height: 1.5px; background: var(--ink); }
  .divider svg { display: block; }
  .contact-detail { font-size: 16px; }

  /* Front side */
  .card-front { left: 636px; top: 122px; width: 420px; height: 638px; }
  .front-mark {
    position: absolute; left: 0; right: 0; top: 0; bottom: 0;
    display: flex; flex-direction: column; align-items: center; justify-content: center;
    gap: 26px; padding-bottom: 40px;
  }
  .front-mark .coin {
    width: 84px; height: 84px; border-radius: 50%;
    background: radial-gradient(circle at 40% 35%, var(--gold), var(--gold-deep));
  }
  .front-mark .brand-name {
    font-family: "Oswald", "Arial Narrow", sans-serif;
    font-weight: 600; font-size: 56px; line-height: 1.05;
    color: var(--steel-light); text-align: center; text-transform: uppercase;
  }
</style>
</head>
<body>

<section class="card card-back" aria-label="Back of business card">
  <svg class="card-shape" width="422" height="628" viewBox="0 0 422 628">
    <path d="M211 5 L417 76 L417 470 Q417 520 375 545 L211 623 L47 545 Q5 520 5 470 L5 76 Z"
          fill="var(--paper)" stroke="var(--ink)" stroke-width="10" stroke-linejoin="miter"/>
  </svg>

  <div class="line headline" style="top:114px">$$$ FREE ATM PLACEMENT $$$</div>
  <div class="benefits-band"><span>BENIFITS OF HAVING AN ATM AT YOUR BUSINESS</span></div>

  <div class="line benefit light" style="top:233px">• FREE ATM and BTM (Bitcoin) installation</div>
  <div class="line benefit light" style="top:252px">maintenance, and loading.</div>
  <div class="line benefit regular" style="top:278px">• Lower card processing fees</div>
  <div class="line benefit regular" style="top:300px">• Ease of access for customers</div>
  <div class="line benefit regular" style="top:322px">• Maintain customers inside location</div>
  <div class="line benefit light" style="top:344px">• Higher tips and spending</div>

  <div class="line contact-heading" style="top:388px">CONTACT ME FOR MORE INFORMATION</div>
  <div class="line owner-name" style="top:428px">Tobias Merlano</div>
  <div class="line owner-title" style="top:462px">OWNER</div>

  <div class="divider">
    <span class="rule"></span>
    <svg width="18" height="18" viewBox="0 0 18 18" aria-label="Phone">
      <rect x="1" y="1" width="16" height="16" rx="3" fill="var(--ink)"/>
      <path d="M4 8 Q9 3 14 8 L13 9.5 L11 8.5 L11 7.5 Q9 6.5 7 7.5 L7 8.5 L5 9.5 Z" fill="var(--paper)"/>
      <rect x="5" y="10" width="8" height="4" rx="1" fill="var(--paper)"/>
    </svg>
    <svg width="18" height="18" viewBox="0 0 18 18" aria-label="Email">
      <rect x="1" y="1" width="16" height="16" rx="3" fill="var(--ink)"/>
      <rect x="4" y="5.5" width="10" height="7" fill="var(--paper)"/>
      <path d="M4 5.5 L9 9.5 L14 5.5" fill="none" stroke="var(--ink)" stroke-width="1"/>
    </svg>
    <span class="rule"></span>
  </div>

  <div class="line contact-detail" style="top:530px">(512) 638-9071 - Call or Text</div>
  <div class="line contact-detail" style="top:551px">Tobias@KioskCoin.example</div>
</section>

<section class="card card-front" aria-label="Front of business card">
  <svg class="card-shape" width="420" height="638" viewBox="0 0 420 638">
    <defs>
      <linearGradient id="steelRim" x1="0" y1="0" x2="1" y2="1">
        <stop offset="0" stop-color="var(--steel-light)"/>
        <stop offset="1" stop-color="var(--steel-dark)"/>
      </linearGradient>
    </defs>
    <path d="M210 0 L420 72 L420 480 Q420 530 378 555 L210 638 L42 555 Q0 530 0 480 L0 72 Z"
          fill="url(#steelRim)"/>
    <path d="M210 14 L406 82 L406 476 Q406 522 366 545 L210 622 L54 545 Q14 522 14 476 L14 82 Z"
          fill="var(--shield-dark)"/>
  </svg>
  <div class="front-mark">
    <span class="coin"></span>
    <div class="brand-name">Kiosk Coin<br>Venture</div>
  </div>
</section>

</body>
</html>
```